Corporate Brochure Cover Design

We need a design for a corporate A4 Size portfolio cover (front and back) which we will be distributing. to our commercial clients.

We are a professional plumbing company that is an industry leader for service we provide to our clients and technology we use. The design needs to incorporate the colours black, red, white and silver and needs to include our logo. We dont have any slogans or mottos... If you wanted to use something it could be "Delivering exceptional service...Always!" however i dont want it to b the focal point of the cover.

Im looking for something professional and modern that has the WOW factor!

Size is A4 - both front and back covers. You can include pictures as well or sample pictures of where we can source and put our own team pictures.

if you have any questions, please do not hesitate to contact me.

Target Market(s)

Our commercial & strata clients - professional industry.

Industry/Entity Type

Commercial

Font styles to use
Sans Serif

Requirements
Must have
• Red, black, white, silver as the colour scheme.
• Include the logo.
Nice to have
• Modern design and something that makes the client go WOW before they open the brochure.
Should not have
• lots of text

```html
<!DOCTYPE html>
<html lang="en">
<head>
<meta charset="utf-8">
<title>Conduit Plumbing – 24/7 Guaranteed Plumbing Services</title>
<link href="https://fonts.googleapis.com/css2?family=Bebas+Neue&family=Open+Sans:wght@300;600;800&display=swap" rel="stylesheet">
<style>
  :root {
    --ink: #231f20;
    --red: #cf0a2c;
    --white: #ffffff;
    --silver: #8a8a8a;
    --silver-light: #e4e6e8;
    --silver-dark: #9da2a7;
    --text-dark: #222222;
  }
  * { box-sizing: border-box; margin: 0; padding: 0; }
  html, body { width: 851px; height: 1200px; overflow: hidden; background: var(--white); }
  .cover {
    position: relative;
    width: 851px;
    height: 1200px;
    overflow: hidden;
    font-family: "Open Sans", Arial, sans-serif;
    background: var(--white);
  }

  /* Header */
  .header {
    position: absolute; left: 0; top: 0; width: 851px; height: 305px;
    background: var(--ink);
  }
  .brand {
    position: absolute; left: 36px; top: 104px;
    display: flex; align-items: center; gap: 14px;
  }
  .brand-mark {
    width: 20px; height: 20px; border-radius: 50%; background: var(--red);
  }
  .brand-name {
    font-weight: 800; font-size: 56px; letter-spacing: 1px;
    color: var(--white); line-height: 1;
  }
  .contact-phone {
    position: absolute; left: 456px; top: 88px;
    display: flex; align-items: center; gap: 16px;
  }
  .phone-icon { width: 74px; height: 74px; display: block; }
  .phone-number {
    font-family: "Bebas Neue", Arial, sans-serif;
    font-size: 58px; color: var(--white); letter-spacing: 0; word-spacing: -4px; line-height: 1;
    padding-top: 6px;
  }
  .contact-email {
    position: absolute; left: 461px; top: 178px;
    font-weight: 600; font-size: 17.5px; color: var(--white);
  }

  /* Tick dividers */
  .ticks {
    position: absolute; left: 20px; width: 815px; height: 9px;
    background: repeating-linear-gradient(90deg, currentColor 0 4px, transparent 4px 13px);
    transform: skewX(-25deg);
  }
  .ticks--light { top: 278px; color: var(--white); }
  .ticks--dark { top: 613px; color: var(--ink); }

  /* Hero */
  .hero-visual {
    position: absolute; left: 32px; top: 305px; width: 468px; height: 295px;
    background: linear-gradient(180deg, var(--silver-light) 0%, var(--silver-dark) 55%, var(--silver-light) 100%);
    border-radius: 0 0 0 60px;
  }
  .service-claim {
    font-family: "Bebas Neue", Arial, sans-serif; line-height: 1; font-weight: 400;
  }
  .claim-line { position: absolute; left: 549px; display: block; white-space: nowrap; }
  .claim-hours { top: 322px; font-size: 128px; letter-spacing: -3px; }
  .claim-hours .red { color: var(--red); }
  .claim-hours .black { color: var(--ink); }
  .claim-hours .grey { color: var(--silver); }
  .claim-guaranteed { top: 452px; font-size: 45px; color: var(--ink); }
  .claim-plumbing { top: 490px; font-size: 62px; color: var(--red); }
  .claim-services { top: 542px; font-size: 64px; color: var(--silver); }

  /* Stats */
  .stats {
    position: absolute; left: 0; top: 632px; width: 851px; height: 568px;
    background: var(--red); color: var(--white); text-align: center;
  }
  .stats-lead {
    position: absolute; left: 0; width: 100%; top: 40px;
    font-weight: 300; font-size: 80px; line-height: 1;
    padding-left: 40px;
  }
  .stats-figure {
    position: absolute; left: 0; width: 100%; top: 132px;
    font-family: "Bebas Neue", Arial, sans-serif;
    font-size: 275px; line-height: 1; letter-spacing: 0;
    padding-left: 14px;
  }
  .stats-label {
    position: absolute; left: 0; width: 100%; top: 394px;
    font-family: "Bebas Neue", Arial, sans-serif;
    font-size: 56px; line-height: 1; color: var(--text-dark);
    letter-spacing: 2px; word-spacing: 10px;
    padding-left: 26px;
  }
  .stats-copy {
    position: absolute; left: 85px; top: 466px; width: 740px; text-align: left;
    font-weight: 300; font-size: 20.5px; line-height: 25px;
  }
</style>
</head>
<body>
<main class="cover">
  <header class="header">
    <div class="brand">
      <span class="brand-mark"></span>
      <span class="brand-name">CONDUIT</span>
    </div>
    <div class="contact-phone">
      <svg class="phone-icon" viewBox="0 0 76 76" aria-hidden="true">
        <circle cx="38" cy="38" r="35" fill="none" stroke="#ffffff" stroke-width="4"/>
        <path d="M27 22c2-2 5-2 6 0l4 7c1 2 0 4-2 5l-2 1c1 4 5 9 9 11l1-2c1-2 3-3 5-2l7 4c2 1 2 4 0 6l-3 3c-2 2-6 2-10 0-7-4-14-11-17-18-2-4-2-8 0-10z" fill="#cf0a2c"/>
      </svg>
      <span class="phone-number">90 12 34 56</span>
    </div>
    <div class="contact-email">service@conduitplumbing.com.au</div>
    <div class="ticks ticks--light"></div>
  </header>

  <section class="hero">
    <div class="hero-visual" role="img" aria-label="Chrome pipe with a red-handled gate valve bending upwards"></div>
    <h1 class="service-claim">
      <span class="claim-line claim-hours"><span class="red">24</span><span class="black">/</span><span class="grey">7</span></span>
      <span class="claim-line claim-guaranteed">Guaranteed</span>
      <span class="claim-line claim-plumbing">Plumbing</span>
      <span class="claim-line claim-services">Services</span>
    </h1>
    <div class="ticks ticks--dark"></div>
  </section>

  <section class="stats">
    <p class="stats-lead">In Excess of</p>
    <p class="stats-figure">100,000</p>
    <p class="stats-label">Successfully Completed Jobs</p>
    <p class="stats-copy">We have achieved over 100,000 successfully completed jobs to date.<br>You can trust that we know the best solution for you.</p>
  </section>
</main>
</body>
</html>
```